Double sided packaging design

Using our logo and its colors, please design a packaging design for our new Product Vitalune.
The printable size is 140mm x 180mm, both sides
Vitalune is a powdered formula of Cinnamon, turmeric, fennel, black pepper, 4 types of kelp & Seaweed, stevia and vanilla.
Its the flavor sensation that energizes your bodies Cells giving them all the food it needs to be healthy.

The old packaging we are moving away from as we have a new formula and we are also marketing for USA
It helps people with pain relief as its proven scientifically to reduce inflammation and other health benefits within the body such as cellular growth.

Please keep to the new colors of the Vitalune Logo as supplied below

Target Market(s)

older women

Industry/Entity Type

Health Suplement Turmeric

Colors
59FF00
82FF00
B8FF75
E3FFCB
F4FFEA
FFC000
F8CF3A
FAE287
FDF2CF
FEFAEE

Requirements
Should not have
• not be too busy

```html
<!DOCTYPE html>
<html lang="en">
<head>
<meta charset="utf-8">
<title>Vitalune Chai Tea – Pouch Front and Back</title>
<link rel="stylesheet" href="https://fonts.googleapis.com/css2?family=Roboto+Slab:wght@400;700;800&family=Quicksand:wght@400;500&family=Yellowtail&display=swap">
<style>
  :root {
    --bg: #e4e6e8;
    --seal: #ffffff;
    --pale: #f4ffea;
    --leaf-pale: #d7eeb4;
    --leaf-mid: #bddc78;
    --leaf: #6fbb2c;
    --leaf-bright: #7cc233;
    --forest: #2d6a1f;
    --forest-dark: #1f5a1c;
    --gold: #f0b400;
    --gold-soft: #f8cf3a;
    --ink-grey: #6d7a6a;
  }
  * { box-sizing: border-box; margin: 0; padding: 0; }
  html, body { width: 1200px; height: 800px; overflow: hidden; }
  body {
    background: var(--bg);
    position: relative;
    font-family: "Roboto Slab", serif;
  }

  .panel {
    position: absolute;
    top: 90px;
    width: 482px;
    height: 620px;
    background: var(--seal);
    overflow: hidden;
    box-shadow: 0 6px 18px rgba(0,0,0,.12);
  }
  .panel--front { left: 90px; }
  .panel--back  { left: 628px; }

  .print {
    position: absolute;
    left: 14px; right: 14px; top: 56px; bottom: 18px;
    background: linear-gradient(180deg, #fbfef6 0%, var(--pale) 22%, var(--leaf-pale) 60%, var(--leaf-mid) 100%);
    overflow: hidden;
  }

  .swoosh { position: absolute; left: 0; width: 100%; display: block; }

  /* brand */
  .brand {
    position: absolute;
    display: flex; align-items: center; gap: 10px;
  }
  .brand__dot {
    width: 34px; height: 34px; border-radius: 50%;
    background: var(--leaf);
  }
  .brand__name {
    font-family: "Roboto Slab", serif;
    font-weight: 400;
    color: var(--gold);
    font-size: 40px;
    letter-spacing: 1px;
  }
  .brand--front { left: 108px; top: 68px; }
  .brand--back { left: 186px; top: 338px; gap: 6px; }
  .brand--back .brand__dot { width: 20px; height: 20px; }
  .brand--back .brand__name { font-size: 22px; }

  /* front */
  .hero {
    position: absolute; left: 0; right: 0; top: 172px; height: 262px;
    background: radial-gradient(ellipse at 55% 45%, #c9cf9a 0%, #7f9b4a 45%, #3f6a2c 100%);
  }
  .product-title {
    position: absolute; left: 18px; top: 200px;
    text-align: center;
  }
  .product-title__name {
    font-weight: 800; font-size: 28px; color: var(--forest);
    -webkit-text-stroke: 1.5px #fff; paint-order: stroke fill;
    line-height: 1;
  }
  .product-title__tag {
    font-weight: 700; font-size: 15px; color: var(--forest);
    -webkit-text-stroke: 1px #fff; paint-order: stroke fill;
    margin-top: 3px;
  }
  .front-info {
    position: absolute; left: 0; right: 0; top: 462px;
    text-align: center; font-weight: 700;
  }
  .front-info__variant { font-size: 15px; color: var(--forest-dark); }
  .front-info__tagline { font-size: 10.5px; color: var(--gold-soft); margin-top: 2px; }
  .front-info__rule {
    width: 220px; margin: 8px auto 5px;
    border-top: 2px dotted var(--forest-dark);
  }
  .front-info__origin { font-size: 11px; color: var(--forest-dark); }
  .front-info__weight { font-size: 10px; color: var(--forest-dark); margin-top: 30px; }

  /* back */
  .copy {
    position: absolute; left: 16px;
    font-family: "Quicksand", sans-serif;
    color: var(--ink-grey);
  }
  .copy__label { font-size: 9px; font-weight: 500; }
  .copy__body { font-size: 7px; line-height: 1.35; }
  .copy--serving { top: 250px; width: 430px; }
  .copy--ingredients { top: 302px; width: 186px; }
  .copy--ingredients .copy__label { font-size: 10px; }

  .pill {
    position: absolute; right: 14px;
    width: 108px; height: 34px; border-radius: 50%;
    background: var(--forest-dark);
    color: #fff;
    font-family: "Yellowtail", cursive;
    font-size: 16px;
    display: flex; align-items: center; justify-content: center;
  }
  .pill--drink { top: 284px; }
  .pill--taste { top: 344px; }

  .contact {
    position: absolute; left: 40px; top: 336px;
    text-align: center; font-weight: 700; font-size: 9px;
    color: var(--forest-dark); line-height: 1.45;
  }
  .maker {
    position: absolute; left: 0; right: 0; top: 398px;
    text-align: center; font-weight: 700; font-size: 7px;
    color: var(--forest-dark); line-height: 1.45;
  }
  .maker__returns { margin-top: 10px; }
</style>
</head>
<body>

<section class="panel panel--front" aria-label="Pouch front">
  <div class="print">
    <div class="brand brand--front">
      <span class="brand__dot"></span>
      <span class="brand__name">Vitalune</span>
    </div>

    <div class="hero" role="img" aria-label="Photo of a relaxed woman with long red hair, hands behind her head, in a sunlit green garden"></div>

    <svg class="swoosh" style="top:150px;height:48px" viewBox="0 0 454 48" preserveAspectRatio="none" aria-hidden="true">
      <path d="M0 6 Q227 48 454 4 L454 14 Q227 58 0 16 Z" fill="var(--leaf-bright)"/>
      <path d="M0 16 Q227 58 454 14 L454 24 Q227 70 0 28 Z" fill="var(--gold)"/>
      <path d="M0 28 Q227 70 454 24 L454 30 Q227 76 0 34 Z" fill="var(--leaf-bright)" opacity=".9"/>
    </svg>

    <div class="product-title">
      <div class="product-title__name">CHAI TEA</div>
      <div class="product-title__tag">-Taste Sensation-</div>
    </div>

    <svg class="swoosh" style="top:418px;height:50px" viewBox="0 0 454 50" preserveAspectRatio="none" aria-hidden="true">
      <path d="M0 22 Q227 -6 454 20 L454 50 L0 50 Z" fill="var(--leaf-mid)"/>
      <path d="M0 22 Q227 -6 454 20 L454 30 Q227 4 0 34 Z" fill="var(--leaf-bright)"/>
      <path d="M0 34 Q227 4 454 30 L454 40 Q227 16 0 44 Z" fill="var(--gold)"/>
    </svg>

    <div class="front-info">
      <div class="front-info__variant">MAREN</div>
      <div class="front-info__tagline">Delicious spices in a unique powder.</div>
      <div class="front-info__rule"></div>
      <div class="front-info__origin">Australian made &amp; owned</div>
      <div class="front-info__weight">342g NET</div>
    </div>
  </div>
</section>

<section class="panel panel--back" aria-label="Pouch back">
  <div class="print">
    <svg class="swoosh" style="top:150px;height:50px" viewBox="0 0 454 50" preserveAspectRatio="none" aria-hidden="true">
      <path d="M0 6 Q227 44 454 0 L454 14 Q227 56 0 18 Z" fill="var(--leaf-bright)"/>
      <path d="M0 18 Q227 56 454 14 L454 26 Q227 70 0 30 Z" fill="var(--gold)"/>
    </svg>

    <div class="copy copy--serving" style="top:196px">
      <div class="copy__label">Serving Suggestion:</div>
      <div class="copy__body">Prepare Vitalune as you would your regular tea - just add to hot water, and let infuse for 1-2 minutes.<br>The screw cap bottle included in the pouch is the recommended serve.</div>
    </div>

    <div class="copy copy--ingredients" style="top:258px;width:190px">
      <div class="copy__label">Ingredients</div>
      <div class="copy__body">Turmeric, Cinnamon, Ground fennel, Vanilla, Calcium carbonate (E170), Sodium biocarbonate (E500), Ascorbic acid (E300), Kelp (0.16g), Black Pepper, Stevia, Green tea, Aniseed, Caraway, Ginger Liquorice, Cloves, Cardamon.</div>
    </div>

    <div class="pill pill--drink" style="top:252px">Drink Turmeric</div>
    <div class="pill pill--taste" style="top:316px">Taste Sensation</div>

    <div class="contact">
      Find us on:<br>info@vitalune.com<br>www.vitalune.com
    </div>

    <div class="brand brand--back">
      <span class="brand__dot"></span>
      <span class="brand__name">Vitalune</span>
    </div>

    <div class="maker">
      <div>Manufactured in Australia for<br>Brightleaf Ventures LLC</div>
      <div class="maker__returns">Product returns<br>Suite 212 Brightleaf Ventures LLC,<br>4820 Harbor View Rd Coral Bay, FL</div>
    </div>

    <svg class="swoosh" style="top:484px;height:62px" viewBox="0 0 454 62" preserveAspectRatio="none" aria-hidden="true">
      <path d="M0 30 Q227 -4 454 26 L454 62 L0 62 Z" fill="var(--leaf-mid)"/>
      <path d="M0 30 Q227 -4 454 26 L454 36 Q227 8 0 42 Z" fill="var(--leaf-bright)"/>
      <path d="M0 42 Q227 8 454 36 L454 48 Q227 22 0 54 Z" fill="var(--gold)"/>
    </svg>
  </div>
</section>

</body>
</html>
```